Crossword App Main Page Design

For a crossword application we need a main page. I am enclosing the current temporary design. There will be 5 buttons. We want a simple but attractive design. Vector designs are preferred. Thank you very much for your interest.
The name of the application is Polyglyph Gridword Riddle and the motto is "gridplay rebuilt." So please use this name on the screen.
Thwe designs I have received so far almost the same with one I have attached. Only the button colors and background image are different. Please try different placement and buttons.
Thanks

```html
<!DOCTYPE html>
<html lang="en">
<head>
<meta charset="utf-8">
<title>Polyglyph Gridword Riddle – Main Menu</title>
<link rel="stylesheet" href="https://fonts.googleapis.com/css2?family=Tinos:ital@0;1&display=swap">
<style>
  :root {
    --paper-top: #e6e4e0;
    --paper-mid: #dddbd7;
    --paper-bottom: #e9e8e4;
    --band: #f0efec;
    --rule: #141414;
    --ink: #0a0a0a;
    --ink-soft: #3a3a3a;
  }
  html, body {
    margin: 0;
    padding: 0;
    width: 815px;
    height: 1200px;
    overflow: hidden;
    background: var(--paper-mid);
  }
  .menu-screen {
    width: 815px;
    height: 1200px;
    position: relative;
    overflow: hidden;
  }
  .menu-screen svg {
    display: block;
    width: 815px;
    height: 1200px;
  }
  .paper-backdrop { fill: url(#paperTone); }
  .menu-band { fill: var(--band); }
  .menu-rule {
    stroke: var(--rule);
    stroke-width: 5;
    fill: none;
    stroke-linejoin: miter;
  }
  .header-rule {
    stroke: var(--rule);
    stroke-width: 3;
  }
  .app-title,
  .app-motto,
  .menu-label {
    font-family: "Tinos", "Times New Roman", serif;
    text-anchor: middle;
  }
  .app-title {
    font-size: 60px;
    fill: var(--ink);
  }
  .app-motto {
    font-size: 34px;
    font-style: italic;
    fill: var(--ink-soft);
  }
  .menu-label { fill: var(--ink); }
  .menu-label--primary { font-size: 104px; }
  .menu-label--secondary { font-size: 80px; }
</style>
</head>
<body>
<main class="menu-screen">
  <svg viewBox="0 0 815 1200" xmlns="http://www.w3.org/2000/svg">
    <defs>
      <linearGradient id="paperTone" x1="0" y1="0" x2="0" y2="1">
        <stop offset="0" stop-color="#e6e4e0"/>
        <stop offset="0.5" stop-color="#dddbd7"/>
        <stop offset="1" stop-color="#e9e8e4"/>
      </linearGradient>
    </defs>

    <rect class="paper-backdrop" x="0" y="0" width="815" height="1200"
          role="img" aria-label="Stacked sheets of white paper seen edge-on, soft grey folds"/>

    <!-- App header -->
    <g class="app-header">
      <text class="app-title" x="407.5" y="118">Polyglyph Gridword Riddle</text>
      <text class="app-motto" x="407.5" y="172">gridplay rebuilt.</text>
      <line class="header-rule" x1="257" y1="204" x2="558" y2="204"/>
    </g>

    <!-- Play: full-width band -->
    <g class="menu-item menu-item--play">
      <polygon class="menu-band" points="0,250 815,246 815,364 0,360"/>
      <line class="menu-rule" x1="0" y1="250" x2="815" y2="246"/>
      <line class="menu-rule" x1="0" y1="360" x2="815" y2="364"/>
      <text class="menu-label menu-label--primary" x="407.5" y="341">PLAY</text>
    </g>

    <!-- My Puzzles: tab from the left -->
    <g class="menu-item menu-item--left">
      <polygon class="menu-band" points="0,436 690,446 690,556 0,546"/>
      <polyline class="menu-rule" points="0,436 690,446 690,556 0,546"/>
      <text class="menu-label menu-label--secondary" x="345" y="524" transform="rotate(0.83 345 496)">My Puzzles</text>
    </g>

    <!-- Buy Puzzles: tab from the right -->
    <g class="menu-item menu-item--right">
      <polygon class="menu-band" points="125,628 815,618 815,728 125,738"/>
      <polyline class="menu-rule" points="815,618 125,628 125,738 815,728"/>
      <text class="menu-label menu-label--secondary" x="470" y="706" transform="rotate(-0.83 470 678)">Buy Puzzles</text>
    </g>

    <!-- About: tab from the left -->
    <g class="menu-item menu-item--left">
      <polygon class="menu-band" points="0,810 690,820 690,930 0,920"/>
      <polyline class="menu-rule" points="0,810 690,820 690,930 0,920"/>
      <text class="menu-label menu-label--secondary" x="345" y="898" transform="rotate(0.83 345 870)">About</text>
    </g>

    <!-- Settings: tab from the right -->
    <g class="menu-item menu-item--right">
      <polygon class="menu-band" points="125,1002 815,992 815,1102 125,1112"/>
      <polyline class="menu-rule" points="815,992 125,1002 125,1112 815,1102"/>
      <text class="menu-label menu-label--secondary" x="470" y="1080" transform="rotate(-0.83 470 1052)">Settings</text>
    </g>
  </svg>
</main>
</body>
</html>
```